Hallo liebe Designer,
wir haben bereits ein Design, welches sich an den Farben unserer Homepage www.lorta.de orientiert. Dieses Design muss nachgebaut werden. Wir benötigen eine editierbare Microsoft-WORD-Datei, die nach Bedarf angepasst werden kann (falls sich Telefonnummer oder ähnliches mal ändert)
Zusammengefasst:
Benötigt wird: Ein Worddokument mit einem Briefpapier mit der Hauptseite und Folgeseiten. Die Folgeseiten sollen automatisch entstehen, wenn mehr wie 1 Seite beschrieben wird.
Das Design bitte so nachbauen wie es im PDF ersichtlich ist.
- das Worddokument muss anpassbar sein, falls sich mal die Telefonnummer o.ä. ändert

```html
<!DOCTYPE html>
<html lang="de">
<head>
<meta charset="utf-8">
<title>LOR Unternehmensgruppe – Briefpapier</title>
<link rel="stylesheet" href="https://fonts.googleapis.com/css2?family=Arimo:wght@400;700&family=Questrial&display=swap">
<style>
  :root {
    --paper: #fefefe;
    --text-grey: #7d7880;
    --brand-green: #9aa89c;
    --brand-dark: #737b70;
    --band-green: #9ea9a0;
    --band-purple: #857985;
    --divider: #9a959c;
  }
  html, body { margin: 0; padding: 0; overflow: hidden; background: var(--paper); }
  .letterhead {
    position: relative;
    width: 846px;
    height: 1200px;
    background: var(--paper);
    overflow: hidden;
    font-family: "Questrial", sans-serif;
    color: var(--text-grey);
  }
  .brand {
    position: absolute;
    right: 56px;
    top: 108px;
    display: flex;
    align-items: center;
    gap: 10px;
    font-family: "Questrial", sans-serif;
    font-size: 23px;
    color: var(--brand-green);
    white-space: nowrap;
  }
  .brand-dot {
    width: 20px; height: 20px;
    border-radius: 50%;
    background: var(--brand-dark);
    flex: none;
  }
  .sender-line {
    position: absolute;
    left: 42px;
    top: 224px;
    margin: 0;
    font-family: "Arimo", sans-serif;
    font-size: 15.6px;
    color: var(--text-grey);
    white-space: nowrap;
  }
  .footer-info {
    position: absolute;
    top: 1089px;
    left: 0;
    width: 846px;
    font-size: 10.5px;
    line-height: 12.2px;
  }
  .footer-col { position: absolute; top: 0; margin: 0; white-space: nowrap; }
  .col-management { left: 42px; }
  .col-bank { left: 213px; }
  .col-contact { left: 414px; }
  .footer-divider {
    position: absolute;
    top: 1089px;
    width: 1px;
    height: 68px;
    background: var(--divider);
  }
  .divider-1 { left: 193px; }
  .divider-2 { left: 397px; }
  .contact-icon { width: 9px; height: 9px; vertical-align: -1px; margin-right: 3px; }
  .footer-band { position: absolute; left: 0; bottom: 0; width: 846px; height: 64px; }
  .website {
    position: absolute;
    right: 54px;
    bottom: 18px;
    margin: 0;
    font-family: "Arimo", sans-serif;
    font-weight: 700;
    font-size: 23px;
    letter-spacing: 0.5px;
    color: #ffffff;
  }
</style>
</head>
<body>
<div class="letterhead">
  <div class="brand">
    <span class="brand-dot"></span>
    <span class="brand-name">LOR Unternehmensgruppe</span>
  </div>

  <p class="sender-line">LOR Unternehmensgruppe GmbH, Lindenweg 42, 63101 Talheim</p>

  <div class="footer-divider divider-1"></div>
  <div class="footer-divider divider-2"></div>

  <div class="footer-info">
    <p class="footer-col col-management">
      Geschäftsführung:<br>
      Markus Verhold<br>
      Sabine Ellring<br>
      Amtsgericht Talheim<br>
      HRB 40817
    </p>
    <p class="footer-col col-bank">
      Umsatzsteuer-ID<br>
      DE000123456<br>
      Sparkasse Rheintal<br>
      BIC: RHTADEXXXXX<br>
      IBAN: DE00 1234 5678 9012 3456 78
    </p>
    <p class="footer-col col-contact">
      Postanschrift:<br>
      Mühlbacher Straße<br>
      42000 Bergfeld<br>
      <svg class="contact-icon" viewBox="0 0 10 10" aria-hidden="true"><path d="M2.2 0.6 L3.8 2.6 L2.9 3.6 Q3.8 5.8 6.3 7.1 L7.3 6.2 L9.3 7.7 L8.3 9.3 Q4.8 9.3 2.3 6.6 Q0.5 4.4 0.6 1.6 Z" fill="var(--text-grey)"/></svg>+49 000 / 12345678<br>
      <svg class="contact-icon" viewBox="0 0 10 10" aria-hidden="true"><rect x="0.6" y="2" width="8.8" height="6.2" fill="none" stroke="var(--text-grey)" stroke-width="0.8"/><path d="M0.6 2 L5 5.6 L9.4 2 M0.6 8.2 L3.8 4.8 M9.4 8.2 L6.2 4.8" fill="none" stroke="var(--text-grey)" stroke-width="0.8"/></svg>info@lorta.de
    </p>
  </div>

  <svg class="footer-band" viewBox="0 0 846 64" aria-hidden="true">
    <rect x="0" y="33" width="846" height="31" fill="var(--band-green)"/>
    <polygon points="593,0 846,0 846,64 552,64" fill="var(--band-purple)"/>
  </svg>
  <p class="website">www.lorta.de</p>
</div>
</body>
</html>
```